Lumen Pact

We teach men how to be successful with women.

We will be putting an Ivendara on the page.

We want to push men to take our 12 month learning program.

Open to ideas and layouts. The website will also be a landing page for our TV campaign.

Lumen pact is a company that will be marketing as an infomercial on late night television and via the internet. 

We will be selling a 12 month program for $997 (paid monthly). It will teach men how to get the woman of their dreams and how attraction is not a choice.
We have systematically developed a program for helping men attract women. 
We do have some competitors but they in the pickup commuinity (Kelo Board, Brett Fenwick and Orbalith Craft are all competitors.
Our website name is lumenpact.com.au.
We will be having an ivendara.com.au on our website to aid the process on making the sale.

The program will be an e-learning program that will be purchased over 12 months.

We also will be selling boot camps in which guys go for a week at a time and train to refine their skills.

Tv

```html
<!DOCTYPE html>
<html lang="en">
<head>
<meta charset="utf-8">
<title>Lumen Pact</title>
<link href="https://fonts.googleapis.com/css2?family=Cabin:wght@400;500&family=Alfa+Slab+One&family=Anton&display=swap" rel="stylesheet">
<style>
:root{
  --black:#000;
  --red:#d90000;
  --red-dark:#b00000;
  --blue:#1a73c9;
  --page:#f6f6f6;
  --text:#555;
  --box:#e6e6e6;
  --white:#fff;
}
*{margin:0;padding:0;box-sizing:border-box}
html,body{width:1200px;height:912px;overflow:hidden}
body{position:relative;background:var(--page);font-family:"Cabin",sans-serif;color:var(--text)}
.header{position:absolute;left:0;top:0;width:1200px;height:94px;background:var(--black)}
.brand{position:absolute;left:186px;top:28px;font-family:"Cabin",sans-serif;font-weight:500;font-size:30px;color:var(--red);white-space:nowrap}
.nav{position:absolute;top:36px;left:444px;display:flex;gap:0;list-style:none}
.nav li{font-size:14.5px;color:var(--white);height:28px;line-height:28px;padding:0 6px}
.nav li.active{background:linear-gradient(#fff,#e4e4e4);color:var(--red);border-radius:3px;padding:0 8px;position:relative}
.nav li.active::after{content:"";position:absolute;left:50%;bottom:-6px;margin-left:-6px;border:6px solid transparent;border-bottom:0;border-top-color:#e4e4e4}
.nav li + li{margin-left:1px}
.zig{position:absolute;left:0;width:1200px;height:6px}
.hero{position:absolute;left:0;top:94px;width:1200px;height:358px;background:linear-gradient(180deg,#c9402a 0%,#e4512a 35%,#f5a334 58%,#b8401f 70%,#1a0d08 82%,#000 100%)}
.headline{position:absolute;right:573px;top:372px;text-align:right;font-family:"Alfa Slab One",serif;font-size:19.5px;line-height:21px;color:var(--white);text-transform:uppercase}
.cta{position:absolute;left:641px;top:377px;width:235px;height:58px;background:linear-gradient(#f01010,#c50000);border:1px solid #ff5a5a;border-radius:4px;font-family:"Anton",sans-serif;font-size:24px;line-height:56px;text-align:center;color:var(--white);text-shadow:1px 1px 2px rgba(0,0,0,.5)}
.feature{position:absolute;top:481px;text-align:left}
.feature .icon{position:absolute;top:0;width:52px;height:52px}
.feature h2{position:absolute;top:62px;font-weight:400;font-size:16px;line-height:19px;color:var(--blue);text-align:center}
.feature p{position:absolute;top:108px;font-size:12px;line-height:15.5px;color:var(--text)}
.divider{position:absolute;top:495px;width:1px;height:160px;background:linear-gradient(transparent,#ddd,transparent)}
.stories-title{position:absolute;left:190px;top:678px;font-size:15px;font-weight:400;color:var(--red)}
.story{position:absolute;left:189px;top:705px;width:615px;height:101px;background:var(--box);border:1px solid #d4d4d4;border-radius:3px;padding:14px 13px;font-size:11.6px;line-height:15.5px;color:#444}
.story cite{display:block;margin-top:8px;font-style:normal}
.presenter{position:absolute;left:844px;top:561px;width:146px;height:269px;background:linear-gradient(180deg,#e9e6e2,#7d88a3 45%,#5f6a86);border-radius:60px 60px 10px 10px}
.footer{position:absolute;left:0;top:830px;width:1200px;height:82px;background:var(--red)}
.foot-nav{position:absolute;left:188px;top:18px;display:flex;gap:15px;list-style:none;font-size:13.7px;color:var(--white)}
.copyright{position:absolute;left:188px;top:42px;font-size:11.5px;color:var(--white)}
.social{position:absolute;top:23px;width:37px;height:37px;background:linear-gradient(#fff,#ddd);border-radius:3px}
</style>
</head>
<body>
<header class="header">
  <div class="brand">Lumen Pact</div>
  <ul class="nav">
    <li class="active">Home</li><li>About us</li><li>Bootcamp</li><li>Learning Program</li><li>Success Stories</li><li>FAQ</li><li>Contact us</li>
  </ul>
</header>
<svg class="zig" style="top:91px" viewBox="0 0 1200 6" preserveAspectRatio="none" aria-hidden="true">
  <defs><pattern id="zigBlack" width="6" height="6" patternUnits="userSpaceOnUse"><path d="M0 0H6L3 6Z" fill="#000"/></pattern></defs>
  <rect width="1200" height="6" fill="#c9402a"/><rect width="1200" height="6" fill="url(#zigBlack)"/>
</svg>

<section class="hero" role="img" aria-label="Sunset seaside photo with a man sitting alone on rocks watching a couple embrace"></section>
<svg class="zig" style="top:91px;position:absolute" width="1200" height="6" aria-hidden="true"><rect width="1200" height="6" fill="url(#zigBlack)"/></svg>
<div class="headline">If you don't start learning<br>to meet hot women<br>when will you?</div>
<div class="cta">MAKE A CHANGE NOW!</div>

<div class="feature" style="left:198px;width:166px">
  <svg class="icon" style="left:55px" viewBox="0 0 52 52" aria-hidden="true"><circle cx="26" cy="26" r="25" fill="#222" stroke="#999" stroke-width="1.5"/><path d="M20 15L37 26L20 37Z" fill="#ddd"/></svg>
  <h2 style="left:0;width:166px">Make a Change<br>Now</h2>
  <p style="left:0;width:175px">Get the Woman of your Dream. Take our 12 month Learning Program. It's Simple</p>
</div>
<div class="divider" style="left:392px"></div>
<div class="feature" style="left:416px;width:170px">
  <svg class="icon" style="left:52px" viewBox="0 0 52 52" aria-hidden="true"><circle cx="26" cy="26" r="25" fill="#222" stroke="#999" stroke-width="1.5"/><path d="M14 33L26 17L38 33Z" fill="#ddd"/><path d="M23 33L26 27L29 33Z" fill="#222"/></svg>
  <h2 style="left:0;width:170px">Join Our<br>Bootcamp Now</h2>
  <p style="left:0;width:170px">Go for a week training &amp; refine your skills. We will train you, how to Get the woman of your Dreams</p>
</div>
<div class="divider" style="left:608px"></div>
<div class="feature" style="left:631px;width:170px">
  <svg class="icon" style="left:57px" viewBox="0 0 52 52" aria-hidden="true"><circle cx="26" cy="26" r="25" fill="#222" stroke="#999" stroke-width="1.5"/><text x="26" y="35" text-anchor="middle" font-family="Cabin,sans-serif" font-size="26" font-weight="500" fill="#ddd">?</text></svg>
  <h2 style="left:0;width:166px">Frequently Asked<br>Questions</h2>
  <p style="left:0;width:170px">Nulla vitae imperdiet elit. Quisque vehicula, nulla sit amet ultrices molestie, purus tortor consequat magna, et eleifend elit quam</p>
</div>

<h3 class="stories-title">Success Stories</h3>
<blockquote class="story">“Praesent sed magna augue, at pulvinar lorem. Ut vulputate mauris ac velit fermentum condimentum. Curabitur vel justo tellus, ut blandit erat. Vestibulum ante ipsum primis in faucibus orci luctus et ultrices posuere cubilia Curae; Aenean libero massa, lacinia elementum pulvinar et, fermentum in odio. Quisque eleifend quam acopi”<cite>Daniel Hart</cite></blockquote>

<div class="presenter" role="img" aria-label="Video presenter: a woman in a grey blazer standing with hands clasped"></div>

<footer class="footer">
  <ul class="foot-nav"><li>Home</li><li>About us</li><li>Bootcamp</li><li>Learning Program</li><li>FAQ</li><li>Success Stories</li><li>Contact us</li></ul>
  <div class="copyright">Copyright © 2013 lumenpact.com.au. All rights reserved</div>
  <div class="social" style="left:880px" aria-label="Social link"></div>
  <div class="social" style="left:923px" aria-label="Social link"></div>
  <div class="social" style="left:966px" aria-label="Social link"></div>
</footer>
<svg class="zig" style="top:827px;position:absolute" width="1200" height="6" aria-hidden="true">
  <defs><pattern id="zigRed" width="6" height="6" patternUnits="userSpaceOnUse"><path d="M0 6H6L3 0Z" fill="#d90000"/></pattern></defs>
  <rect width="1200" height="6" fill="url(#zigRed)"/>
</svg>
</body>
</html>
```